Delmer's Pressure Washing Services

Starting a pressure washing business on my own in Central Valley California, not too much experience so affordable, I do houses, fences, driveways, cars, trailers, RVs. Planning to make this full-time hoping clientele picks up after having a nice business card. Design doesn't have to be flashy, more to the point, I like simplistic/personable. I do not want something exhausting to look at or with too much going on.

Target Market(s)

Residential, Commercial

Industry/Entity Type

Pressure Washing

Contact Information for Business Card

avalible Services

Font styles to use
Sans Serif

Colors
0054AA
0677BA
7BADD7
CADEEF
E8F1F8
0094D4
00A9DD
6FCCEA
C7EBF8
E9F6FB
00AB8E
00BBA5
67D7C9
C6EFE9
E9F9F6

```html
<!DOCTYPE html>
<html lang="en">
<head>
<meta charset="utf-8">
<title>Delmer's Pressure Washing Services – Business Card</title>
<link rel="stylesheet" href="https://fonts.googleapis.com/css2?family=Michroma&display=swap">
<style>
  :root {
    --backdrop: #8a6f52;
    --card-white: #ffffff;
    --brand-blue: #1d5bad;
    --deep-blue: #14479e;
    --sky-blue: #0094d4;
    --accent-orange: #c4832a;
    --text-light: #ffffff;
  }
  * { margin: 0; padding: 0; box-sizing: border-box; }
  html, body { width: 900px; height: 1200px; overflow: hidden; }
  body {
    background: var(--backdrop);
    font-family: "Michroma", "Arial", sans-serif;
    position: relative;
  }
  .card {
    position: absolute;
    left: 73px;
    width: 760px;
    height: 446px;
    border-radius: 32px;
    overflow: hidden;
  }
  .card-front { top: 112px; background: var(--card-white); }
  .card-back  { top: 637px; background: var(--deep-blue); }

  .front-shapes { position: absolute; inset: 0; }

  .wordmark {
    position: absolute;
    left: 0; right: 0;
    text-align: center;
    line-height: 1.15;
  }
  .wordmark .line-main { font-size: 54px; letter-spacing: 1px; }
  .wordmark .line-sub  { font-size: 25px; letter-spacing: 0.5px; }
  .wordmark .line-tail { font-size: 20px; letter-spacing: 1px; }
  .front-wordmark { top: 78px; color: var(--brand-blue); }
  .back-wordmark  { top: 160px; color: var(--text-light); }
  .wordmark .mark-dot {
    display: inline-block;
    width: 14px; height: 14px;
    border-radius: 50%;
    background: currentColor;
    margin-left: 10px;
    vertical-align: middle;
  }

  .owner {
    position: absolute;
    top: 293px; left: 0; right: 0;
    text-align: center;
    color: var(--text-light);
  }
  .owner-name { font-size: 28px; letter-spacing: 1px; }
  .owner-phone {
    margin-top: 8px;
    font-size: 18px;
    display: flex;
    justify-content: center;
    align-items: center;
    gap: 6px;
  }
  .owner-phone svg { width: 16px; height: 16px; }

  .service-list {
    position: absolute;
    top: 408px; left: 0; right: 0;
    text-align: center;
    color: var(--text-light);
    font-size: 15.5px;
    letter-spacing: 0.3px;
  }
</style>
</head>
<body>

<section class="card card-front">
  <svg class="front-shapes" viewBox="0 0 760 446" aria-hidden="true">
    <path d="M10,212 Q380,330 750,210" fill="none" stroke="var(--accent-orange)" stroke-width="5"/>
    <path d="M0,220 Q380,345 760,217 L760,380 Q380,358 0,384 Z" fill="var(--brand-blue)"/>
    <path d="M0,392 Q380,366 760,387 L760,446 L0,446 Z" fill="var(--accent-orange)"/>
  </svg>

  <div class="wordmark front-wordmark">
    <div class="line-main">DELMER'S<span class="mark-dot"></span></div>
    <div class="line-sub">PRESSURE WASHING</div>
    <div class="line-tail">SERVICES</div>
  </div>

  <div class="owner">
    <div class="owner-name">DELMER RUIZ</div>
    <div class="owner-phone">
      <svg viewBox="0 0 24 24" aria-hidden="true"><path fill="#fff" d="M6.6 10.8a15.1 15.1 0 0 0 6.6 6.6l2.2-2.2a1 1 0 0 1 1-.25 11.4 11.4 0 0 0 3.6.57 1 1 0 0 1 1 1V20a1 1 0 0 1-1 1A17 17 0 0 1 3 4a1 1 0 0 1 1-1h3.5a1 1 0 0 1 1 1c0 1.25.2 2.45.57 3.57a1 1 0 0 1-.25 1z"/></svg>
      <span>2099 555 014</span>
    </div>
  </div>

  <div class="service-list">HOUSES • FENCES • DRIVEWAYS • CARS • TRAILERS • RVS</div>
</section>

<section class="card card-back">
  <div class="wordmark back-wordmark">
    <div class="line-main">DELMER'S<span class="mark-dot"></span></div>
    <div class="line-sub">PRESSURE WASHING</div>
    <div class="line-tail">SERVICES</div>
  </div>
</section>

</body>
</html>
```